Price List Modified

We have a price list in PDF that we need changed. The current price list is in Euro's and we need the Euro's changed to U.S. dollars. We simply use a conversion factor of 1.55 for this.

We also need the dimensions of units converted from MM to inches.

Industry/Entity Type

Graphic Design

```html
<!DOCTYPE html>
<html lang="en">
<head>
<meta charset="utf-8">
<title>Pressure Steamer – Price List</title>
<link href="https://fonts.googleapis.com/css2?family=Roboto+Condensed:wght@300;400;700&family=Archivo+Black&display=swap" rel="stylesheet">
<style>
  :root{
    --green:#2e9e3e;
    --ink:#1a1a1a;
    --soft:#555;
    --rule:#bdbdbd;
    --steel:#c9ccce;
    --steel-dark:#8d9295;
    --paper:#ffffff;
  }
  *{margin:0;padding:0;box-sizing:border-box}
  html,body{width:849px;height:1200px;overflow:hidden;background:var(--paper)}
  body{position:relative;font-family:"Roboto Condensed",Arial,sans-serif;color:var(--ink)}
  .abs{position:absolute}
  .page-title{left:48px;top:46px;font-size:13px;font-weight:700;line-height:15px}
  .page-title span{display:block;font-weight:400}
  .icon-power{left:48px;top:117px}
  .model-name{left:228px;top:110px;font-size:28px;line-height:30px}
  .model-name b{font-family:"Archivo Black",Arial,sans-serif;font-weight:400}
  .model-name span{font-weight:300}
  .rule-green{left:48px;width:752px;height:4px;background:var(--green)}
  .rule-thin{height:1px;background:var(--rule)}
  .th{font-size:10px;line-height:11px}
  .th i{display:block;font-style:normal;color:var(--soft)}
  .colsep{width:1px;background:#ddd}
  .cell{font-size:10px;line-height:11px}
  .code{font-size:11px;font-weight:700}
  .sub{display:block;color:var(--soft);font-size:9px}
  .price{font-size:9px;font-weight:700}
  .note{left:228px;top:272px;font-size:10px;line-height:11px}
  .note b{font-weight:700}
  .photo{background:linear-gradient(180deg,#e4e6e7,var(--steel) 60%,var(--steel-dark))}
  .drawing{background:linear-gradient(180deg,#f4f4f4,#e2e2e2)}
  .caption{font-size:10px;left:48px}
  .section-title{left:226px;top:584px;font-size:13px}
  .section-title b{font-weight:700}
  .page-no{right:48px;top:1166px;font-size:15px}
</style>
</head>
<body>
  <div class="abs page-title">FORNO A VAPORE A PRESSIONE<span>PRESSURE STEAMER</span></div>

  <svg class="abs icon-power" width="17" height="14" viewBox="0 0 17 14" aria-label="Electric">
    <rect x="0.5" y="0.5" width="16" height="13" fill="none" stroke="#1a1a1a"/>
    <rect x="2" y="2" width="13" height="10" fill="#1a1a1a"/>
    <path d="M9.5 3 L6 7.5 H8.5 L7 11 L11 6 H8.5 Z" fill="#fff"/>
  </svg>

  <div class="abs model-name"><b>PSV</b> <span>410</span></div>
  <div class="abs rule-green" style="top:139px"></div>

  <!-- main table header -->
  <div class="abs th" style="left:233px;top:149px">Codice<i>Code</i></div>
  <div class="abs th" style="left:293px;top:149px">Versione<i>Version</i></div>
  <div class="abs th" style="left:385px;top:149px">Capacità<i>Capacity</i></div>
  <div class="abs th" style="left:459px;top:149px">Passo guide<i>Distance guides</i></div>
  <div class="abs th" style="left:528px;top:149px">Dimensioni inch<i>Dimensions inch</i></div>
  <div class="abs th" style="left:605px;top:149px">Peso<i>Weight</i></div>
  <div class="abs th" style="left:649px;top:149px">Power V/50Hz</div>
  <div class="abs th" style="left:745px;top:149px">$</div>
  <div class="abs colsep" style="left:288px;top:146px;height:28px"></div>
  <div class="abs colsep" style="left:380px;top:146px;height:28px"></div>
  <div class="abs colsep" style="left:454px;top:146px;height:28px"></div>
  <div class="abs colsep" style="left:523px;top:146px;height:28px"></div>
  <div class="abs colsep" style="left:600px;top:146px;height:28px"></div>
  <div class="abs colsep" style="left:644px;top:146px;height:28px"></div>
  <div class="abs colsep" style="left:740px;top:146px;height:28px"></div>

  <div class="abs photo" role="img" aria-label="Pressure steamer product photo" style="left:48px;top:208px;width:137px;height:142px"></div>
  <div class="abs caption" style="top:362px">PSV 410 E</div>

  <div class="abs code" style="left:233px;top:227px">PSV 410 E</div>
  <div class="abs cell" style="left:293px;top:222px">Elettronica<span class="sub">Electronic</span></div>
  <div class="abs cell" style="left:385px;top:227px"><b style="font-size:13px">3</b> x GN 1/1</div>
  <div class="abs cell" style="left:459px;top:228px">3.2 inch</div>
  <svg class="abs" style="left:492px;top:219px" width="16" height="26" viewBox="0 0 16 26" aria-label="Distance between guides">
    <path d="M2 2 H14 M2 24 H14" stroke="#555" stroke-dasharray="2 2"/>
    <path d="M8 4 V22 M5 7 L8 4 L11 7 M5 19 L8 22 L11 19" stroke="#1a1a1a" fill="none"/>
  </svg>
  <div class="abs cell" style="left:528px;top:228px;font-size:9px">27.2x34.8x28 h</div>
  <div class="abs cell" style="left:605px;top:228px;font-size:9px">110 Kg</div>
  <div class="abs cell" style="left:649px;top:228px;font-size:9px">kW 15,5 3N AC 400V</div>
  <div class="abs colsep" style="left:600px;top:210px;height:52px"></div>
  <div class="abs colsep" style="left:644px;top:210px;height:52px"></div>
  <div class="abs colsep" style="left:740px;top:210px;height:52px"></div>
  <div class="abs price" style="left:745px;top:229px">19,840.00</div>
  <div class="abs rule-thin" style="left:228px;top:262px;width:572px"></div>

  <div class="abs note"><b>NOTA:</b> se la durezza dell'acqua è superiore a 3°dH, è consigliato l'utilizzo del sistema di filtraggio WFS2200 (vedere optionals)<br>NOTE: if water hardness exceeds 3°dH, a WFS2200 water filter system should be installed (see optionals)</div>

  <!-- optionals -->
  <div class="abs section-title"><b>PSV OPTIONAL</b> OPTIONALS</div>
  <div class="abs rule-green" style="top:599px"></div>
  <div class="abs th" style="left:233px;top:608px">Codice<i>Code</i></div>
  <div class="abs th" style="left:293px;top:608px">Descrizione<i>Description</i></div>
  <div class="abs th" style="left:528px;top:608px">Dimensioni inch<i>Dimensions inch</i></div>
  <div class="abs th" style="left:657px;top:608px">Peso<i>Weight</i></div>
  <div class="abs th" style="left:745px;top:608px">$</div>
  <div class="abs colsep" style="left:288px;top:605px;height:28px"></div>
  <div class="abs colsep" style="left:523px;top:605px;height:28px"></div>
  <div class="abs colsep" style="left:652px;top:605px;height:28px"></div>
  <div class="abs colsep" style="left:740px;top:605px;height:28px"></div>

  <div class="abs drawing" role="img" aria-label="Water filter cartridge illustration" style="left:48px;top:683px;width:40px;height:64px"></div>
  <div class="abs caption" style="top:756px">WFS 2200</div>
  <div class="abs code" style="left:233px;top:698px">WFS 2200</div>
  <div class="abs cell" style="left:293px;top:693px">Sistema filtraggio acqua<span class="sub">Water filter system</span></div>
  <div class="abs cell" style="left:528px;top:701px;font-size:9px">7.36x7.36x22.12 h</div>
  <div class="abs cell" style="left:657px;top:701px;font-size:9px">7,7 Kg</div>
  <div class="abs price" style="left:745px;top:702px">883.50</div>
  <div class="abs rule-thin" style="left:228px;top:722px;width:572px"></div>

  <div class="abs drawing" role="img" aria-label="Support base stand drawing" style="left:48px;top:788px;width:93px;height:105px"></div>
  <div class="abs caption" style="top:903px">SBS 410</div>
  <div class="abs code" style="left:233px;top:803px">SBS 410</div>
  <div class="abs cell" style="left:293px;top:797px">Supporto con ripiano di fondo<span class="sub">Support base</span></div>
  <div class="abs cell" style="left:528px;top:804px;font-size:9px">27.2x29.2x36 h</div>
  <div class="abs cell" style="left:657px;top:804px;font-size:9px">15 Kg</div>
  <div class="abs price" style="left:745px;top:805px">651.00</div>
  <div class="abs rule-thin" style="left:228px;top:824px;width:572px"></div>

  <div class="abs drawing" role="img" aria-label="Cabinet base with tray rack drawing" style="left:48px;top:922px;width:93px;height:110px"></div>
  <div class="abs caption" style="top:1042px">CBS 410</div>
  <div class="abs code" style="left:233px;top:940px">CBS 410</div>
  <div class="abs cell" style="left:293px;top:935px">Armadio con ripiano di fondo e struttura<br>portateglie<span style="color:var(--soft);font-size:9px">Support base</span></div>
  <div class="abs cell" style="left:528px;top:941px;font-size:9px">27.2x29.2x36 h</div>
  <div class="abs cell" style="left:657px;top:941px;font-size:9px">64 Kg</div>
  <div class="abs price" style="left:745px;top:942px">2,294.00</div>
  <div class="abs rule-thin" style="left:228px;top:961px;width:572px"></div>

  <div class="abs drawing" role="img" aria-label="USB port device illustration" style="left:48px;top:1074px;width:60px;height:38px"></div>
  <div class="abs caption" style="top:1124px">USB 10X</div>
  <div class="abs code" style="left:233px;top:1080px">USB 10X</div>
  <div class="abs cell" style="left:293px;top:1075px">Porta USB salvataggio dati HACCP<span class="sub">USB port saving device HACCP</span></div>
  <div class="abs colsep" style="left:513px;top:1070px;height:29px"></div>
  <div class="abs colsep" style="left:740px;top:1070px;height:29px"></div>
  <div class="abs price" style="left:745px;top:1081px">124.00</div>
  <div class="abs rule-thin" style="left:228px;top:1099px;width:572px"></div>

  <div class="abs" style="left:48px;top:1150px;width:752px;height:1px;background:var(--green)"></div>
  <div class="abs page-no">53</div>
</body>
</html>
```